Redesign of existing site - Velbrin GmbH

Redesign of the following site.
https://www.velbrin-gmbh.example/

The colors red and green need to remain.
Topic: calendar binder

The font "FF Market Regular" should be used s well. But -- if you find a font which is similar and a bit more modern, then go with it. (see font-example.jpg)

The mainpage should have a slider with a video first. Enclosed is a screenshot of the video. (see video.jpg)

Logo also enclosed as svg. The red color might not be quit right. Please check it on your own.
For the second page this page should be used to redesign:
https://www.velbrin-gmbh.example/bindungen/ring-wire-bindung/

I am planing to use the DIVI builder. If you built this in DIVI builder and be able to send me the template or installation (Duplicator) that would be a huge advantage.
Updates

IMPORTANT:
I have received many designs in English. But I can't present them to the customer. Please convert them into German, otherwise they cannot be used.

Requirements
Must have
• Please translate designs into german if it is to be considered. How should I explain a design in english to the customer?

```html
<!DOCTYPE html>
<html lang="de">
<head>
<meta charset="utf-8">
<title>Velbrin Kalenderbindungen</title>
<link href="https://fonts.googleapis.com/css2?family=Montserrat:wght@400;500;600&family=Mrs+Saint+Delafield&display=swap" rel="stylesheet">
<style>
:root{
  --red:#ee1111;
  --green:#6cbd2c;
  --ink:#222;
  --muted:#777;
  --gray:#efefef;
  --dark:#141213;
  --social:#3a3839;
  --white:#fff;
}
*{box-sizing:border-box;margin:0;padding:0}
html,body{width:1200px;height:2692px;overflow:hidden}
body{position:relative;font-family:'Montserrat',sans-serif;color:var(--ink);background:var(--white)}
.script{font-family:'Mrs Saint Delafield',cursive;font-weight:400}
.btn{position:absolute;display:flex;align-items:center;justify-content:center;background:var(--green);color:var(--white);border-radius:22px;font-weight:600;font-size:14px;text-decoration:none}

/* header */
.site-header{position:absolute;left:0;top:0;width:1200px;height:113px;background:#f7f7f7;border-bottom:1px solid #ddd}
.brand{position:absolute;left:89px;top:33px;font-family:'Montserrat',sans-serif;font-weight:600;color:var(--red);font-size:38px;line-height:46px}
.nav{position:absolute;right:262px;top:45px;display:flex;gap:22px;font-size:15px;color:#555}
.nav a{color:#555;text-decoration:none}

/* hero */
.hero{position:absolute;left:0;top:113px;width:1200px;height:585px;background:linear-gradient(160deg,#4b4746 0%,#2b2929 45%,#5e5a58 75%,#3a3636 100%)}
.hero-title{position:absolute;left:0;width:1200px;top:100px;text-align:center;color:var(--white);font-size:100px;line-height:76px}
.scroll-mouse{position:absolute;left:578px;top:488px}

/* intro */
.section-title{position:absolute;left:0;width:1200px;text-align:center;font-size:56px;line-height:60px;color:var(--ink)}
.lead{position:absolute;font-size:15px;line-height:22px;color:var(--muted);text-align:center}
.card{position:absolute;background:var(--white);border-radius:14px;box-shadow:0 4px 24px rgba(0,0,0,.07);text-align:center}
.card-icon{width:90px;height:90px;border-radius:50%;margin:22px auto 0}
.card h3{font-weight:500;font-size:19px;margin-top:14px}
.card p{font-size:15px;line-height:22px;color:var(--muted);margin:10px 18px 0}

/* browsing */
.browse{position:absolute;left:0;top:1272px;width:1200px;height:575px;background:var(--gray)}
.product{position:absolute;top:149px;width:242px;text-align:center}
.product-photo{width:242px;height:239px;border-radius:12px}
.product h4{font-weight:500;font-size:19px;margin-top:16px}
.product a{display:block;color:var(--red);font-size:14px;font-weight:500;margin-top:5px;text-decoration:underline}

/* stats */
.stat h3{font-weight:500;font-size:22px;margin-top:18px}
.stat .num{font-size:38px;line-height:40px;margin-top:4px}
.stat p{font-size:16px;color:var(--ink);margin-top:4px}

/* footer */
.site-footer{position:absolute;left:0;top:2156px;width:1200px;height:536px;background:var(--dark);color:#ddd}
.footer-brand{position:absolute;left:113px;top:88px;font-family:'Montserrat',sans-serif;font-weight:600;color:var(--red);font-size:56px;line-height:70px}
.footer-about{position:absolute;left:113px;top:215px;width:340px;font-size:14.5px;line-height:22px}
.footer-about p{margin-bottom:6px}
.footer-head{position:absolute;font-size:48px;line-height:56px;color:var(--white)}
.footer-text{position:absolute;font-size:14.5px;line-height:22px}
.contact-row{position:absolute;left:892px;display:flex;gap:14px;font-size:14.5px;line-height:22px}
.social{position:absolute;top:2461px;width:44px;height:44px;border-radius:50%;background:var(--social)}
.rule{position:absolute;left:89px;width:1022px;height:1px;background:#777}
.copyright{position:absolute;left:0;width:1200px;text-align:center;font-size:14.5px;color:#eee}
</style>
</head>
<body>

<header class="site-header">
  <div class="brand">Velbrin</div>
  <nav class="nav"><a>Start</a><a>Unternehmen</a><a>Bindungen</a><a>Exklusiv</a><a>Galerie</a><a>Service</a></nav>
  <a class="btn" style="left:971px;top:35px;width:140px;height:42px;font-size:15px">Kontakt</a>
</header>

<section class="hero" role="img" aria-label="Kalenderbindemaschinen in einer Produktionshalle">
  <h1 class="hero-title script">Willkommen bei<br>Velbrin Kalenderbindungen</h1>
  <a class="btn" style="left:481px;top:284px;width:238px;height:42px">Jetzt Angebot anfordern</a>
  <svg class="scroll-mouse" width="44" height="72" viewBox="0 0 44 72">
    <rect x="1.5" y="1.5" width="41" height="69" rx="20.5" fill="none" stroke="#fff" stroke-width="2"/>
    <path d="M22 28v22M16 44l6 6 6-6" fill="none" stroke="#fff" stroke-width="2"/>
  </svg>
</section>

<h2 class="section-title script" style="top:770px">Service aus einer Hand – Kompetenz verbindet!</h2>
<p class="lead" style="left:190px;top:834px;width:820px">Velbrin – der Name steht für höchste Qualität und Erfahrung bei allen plan liegenden Kalender- und Broschürenbindungen. Seit über 50 Jahren beraten wir Kunden im In- und Ausland kreativ zu allen Fragen rund um Gestaltung und Funktion ihrer Produkte.</p>

<div class="card" style="left:165px;top:930px;width:253px;height:250px">
  <div class="card-icon" style="background:var(--red)" role="img" aria-label="Symbol für Exklusivität"></div>
  <h3>Exklusiv</h3>
  <p>Außergewöhnliche Aufgaben sind unser Fach, Exklusivität ist unser Markenzeichen.</p>
</div>
<div class="card" style="left:438px;top:930px;width:323px;height:250px">
  <div class="card-icon" style="background:var(--green)" role="img" aria-label="Symbol für Technik"></div>
  <h3>Technische Informationen</h3>
  <p>Wenn Sie ins Detail gehen möchten, helfen wir Ihnen gern. So präsentieren Sie Ihre Produkte...</p>
</div>
<div class="card" style="left:781px;top:930px;width:253px;height:250px">
  <div class="card-icon" style="background:var(--red)" role="img" aria-label="Symbol für das Team"></div>
  <h3>Unser Team</h3>
  <p>Seit über 50 Jahren beraten wir Kunden im In- und Ausland...</p>
</div>

<section class="browse">
  <h2 class="section-title script" style="top:38px">Bequem durchblättern!</h2>
  <p class="lead" style="left:0;top:112px;width:1200px">Unsere Kalenderbindungen und Bindungen auf einen Blick.</p>
  <div class="product" style="left:89px">
    <div class="product-photo" role="img" aria-label="Orangefarbene Ring-Wire-Bindung in Nahaufnahme" style="background:linear-gradient(135deg,#2a2624,#c8742e 50%,#d9d6d2)"></div>
    <h4>Ring-Wire-Bindung</h4><a>Mehr Infos</a>
  </div>
  <div class="product" style="left:349px">
    <div class="product-photo" role="img" aria-label="Schwarze Spiralbindung an weißen Seiten" style="background:linear-gradient(135deg,#c9d4e0,#8e99a6 50%,#e9edf1)"></div>
    <h4>Spiralbindung</h4><a>Mehr Infos</a>
  </div>
  <div class="product" style="left:609px">
    <div class="product-photo" role="img" aria-label="Rote Leinenfalz-Streifen" style="background:linear-gradient(160deg,#a51a1a,#d9dde2 45%,#a51a1a 70%,#c9ccd0)"></div>
    <h4>Leinenfalz</h4><a>Mehr Infos</a>
  </div>
  <div class="product" style="left:869px">
    <div class="product-photo" role="img" aria-label="Gefalteter Tischkalender mit blauem Druck" style="background:linear-gradient(135deg,#5c5f66,#e6e8ec 45%,#1e5fcc 85%)"></div>
    <h4>Faltfalz</h4><a>Mehr Infos</a>
  </div>
  <a class="btn" style="left:522px;top:482px;width:156px;height:42px;font-size:15px">Mehr anzeigen</a>
</section>

<div class="card stat" style="left:165px;top:1928px;width:253px;height:133px">
  <h3>Über</h3><div class="num script">+ 56</div><p>Jahre Erfahrung</p>
</div>
<div class="card stat" style="left:438px;top:1928px;width:323px;height:133px">
  <h3>Zufriedene</h3><div class="num script">+ 1547</div><p>Kunden</p>
</div>
<div class="card stat" style="left:781px;top:1928px;width:253px;height:133px">
  <h3>Mehr als</h3><div class="num script">65 Millionen+</div><p>Bindungen</p>
</div>

<footer class="site-footer">
  <div class="footer-brand">Velbrin</div>
  <div class="footer-about">
    <p>Der Druckweiterverarbeiter Velbrin ist einer der größten Kalenderhersteller Deutschlands, mit vier vollautomatischen Kalenderlinien.</p>
    <p>Als Industriebuchbinderei fertigt Velbrin großformatige Kalender bis 1,60 Meter Länge.</p>
    <p>Drei Fertigungslinien stehen für Bücher, Broschüren, Wochenkalender, Tischaufsteller und Notizbücher bereit.</p>
  </div>

  <h3 class="footer-head script" style="left:523px;top:66px">Adresse</h3>
  <p class="footer-text" style="left:523px;top:128px;width:280px">Velbrin GmbH &amp; Co. KG Lindenhofweg 14, 84112 Auwiesen</p>

  <h3 class="footer-head script" style="left:523px;top:262px">Rechtliches</h3>
  <p class="footer-text" style="left:523px;top:324px">Impressum<br>Cookies Datenschutz</p>

  <h3 class="footer-head script" style="left:892px;top:66px">Kontakt</h3>
  <div class="contact-row" style="top:128px">
    <svg width="16" height="16" viewBox="0 0 24 24" style="margin-top:4px"><path fill="#fff" d="M6.6 10.8a15.1 15.1 0 0 0 6.6 6.6l2.2-2.2c.3-.3.7-.4 1-.2 1.1.4 2.3.6 3.6.6.6 0 1 .4 1 1V20c0 .6-.4 1-1 1A17 17 0 0 1 3 4c0-.6.4-1 1-1h3.5c.6 0 1 .4 1 1 0 1.3.2 2.5.6 3.6.1.3 0 .7-.2 1z"/></svg>
    <span>Telefon:<br>+49 (0000) 4821-0</span>
  </div>
  <div class="contact-row" style="top:186px">
    <svg width="16" height="16" viewBox="0 0 24 24" style="margin-top:4px"><path fill="#fff" d="M2 5h20v2l-10 6L2 7zM2 9l10 6 10-6v10H2z"/></svg>
    <span>E-Mail:<br>info@velbrin-gmbh.example</span>
  </div>

  <div class="rule" style="top:461px"></div>
  <p class="copyright" style="top:489px">© 2025 Velbrin GmbH &amp; Co. KG - Ring-Wire-Bindungen - Drahtkammbindungen - Kalenderbindungen - Auwiesen</p>
</footer>

<span class="social" style="left:889px;background:var(--red)" aria-label="Soziales Profil"></span>
<span class="social" style="left:944px" aria-label="Soziales Profil"></span>
<span class="social" style="left:996px" aria-label="Soziales Profil"></span>
<span class="social" style="left:1043px" aria-label="Soziales Profil"></span>

</body>
</html>
```